Wren Motorcar Polishing Flyer Design

Hi, I need a flyer design for the pricing and package display of my business (Wren Motorcar Polishing)

www.kelvora.example/wrenmotorpolish

To keep this short and simple, I will need 2 versions of your finished product, can be similar in design just has to be saying something different.

First flyer will be the general version for all customers.

It will need to include the following!
Format, Placement, Font, Design etc.. is all up to you!

==================================

Package 1 [Cars $49.99][Trucks Vans & SUV's $54.99]: Speed Detail

- Exterior Pressure Clean w/ Spotless water
treatment and Vacuum dried
- Wheel Wells Glossed and Cleaned
- Tires Cleaned and Hand Dried
- Tires Dressed with Gloss Finish
- Exterior and Interior Windows cleaned and Hand Dried
- Interior is Vacuumed and Door jams cleaned to Perfection!

Package 2 [Cars $59.99][Trucks Vans & SUV's $64.99]: Speed Detail & Hand Waxing

- Exterior Pressure Clean w/ Spotless water treatment and Vacuum dried
- Hand Applied Wax Treatment with Delmark's Advanced Spray on wax & Micro Scratch Sealant!

Package 3 [Cars $110.00][Trucks Vans & SUV's $149.99]: Advanced Interior Detail

- Interior & Exterior Windows Cleaned and Hand Dried
- All Vents and Creases cleaned out
- Advanced plastic/vinyl/leather Vellusta Interior Treatment!
- Plastic/Vinyl/Leather Conditioner Vellusta Treatment
- Hand Treated Dust Removal
- Seats/Carpets/Headliner steam cleaned
- Seat Belts/Trunks & Floor Mats Treated and Rejuvenated
- Stain Removal

Package 4 [Cars $110.00][Trucks Vans & SUV's $149.99]: Advanced Exterior Detail

- Exterior Pressure Clean w/ Spotless water treatment and Vacuum dry with additional Hand Drying
- Hand Applied Carnauba Wax & Micro Scratch Sealant Treatment
- Dark Exterior Plastic Restoration Treatment (wherever applicable)

Package 5 [Cars $210][Trucks Vans & SUV's $299.99];The Complete Detail

- Stain Removal

Additional Options (May be applied to existing packages when requested!):

(Clay Bar Treatment): [Cars $69.99][Trucks Vans & SUV's $99.99]

- Removal of all Build-Up on Paint such as Micro debris, stone chips, water spots

(Full Vehicle Polishing): [Cars $75.99][Trucks Vans & SUV's $119.99]

- This process removes marring, swirl marks, scratches, stone chips, water spots and acid etching caused by bird droppings and bug remains.

- Adds a sleek shine when wax is applied after.

(Drop-Q Hand Applied Window Treatment): [Cars $10.00][Trucks Vans & SUV's $15]

- This process repels water, making windshield wipers unneeded during storms and rainy weather.

A percentage of proceeds will be Donated to Help Veterans in need!

Phone #: xxx-xxx-xxxx
Email #: xxxxxxxxxx
Instagram: @
Facebook: kelvora.example/wrenmotorpolish
website: > Coming Soon <

Alright, that will be the first designed flyer.

The next flyer can be single paged or flyer layed out. It is generally aimed towards my first customer Lindqvist Strength and Care. An image of there logo will be provided below along with my logo and current business card so ideas can be drawn beside them.

Wren Motorcar Polishing
The Lindqvist Special (For August)

Package 1 [Cars $24.99][Trucks Vans & SUV's $34.99]: Speed Detail

Package 2 [Cars $39.99][Trucks Vans & SUV's $44.99]: Speed Detail & Hand Waxing

Thanks a TON! If you guy's need anymore information or have any other questions during the design process, please, please; let me know!

Target Market(s)

Automotive Detailing, Mobile Automotive Detailing, Parking Lot Detailing, Business Detailing, etc.

Industry/Entity Type

Automotive

Requirements
Must have
• A Classy Design, I'd like it to match in some form or another the Card pictures I have submitted
Nice to have
• Black and White as primary colors, silver aswell
Should not have
• Not too much Wren orange coloring in the design unless it adds to the overall definition of the finished project. Thanks!

```html
<!DOCTYPE html>
<html lang="en">
<head>
<meta charset="utf-8">
<title>The Lindqvist Special – Wren Motorcar Polishing</title>
<link href="https://fonts.googleapis.com/css2?family=Lato:wght@400;700;900&display=swap" rel="stylesheet">
<style>
  :root {
    --page-bg: #e4e4e4;
    --flyer-bg: #1b1b1d;
    --orange: #f58220;
    --white: #ffffff;
    --ink: #111111;
    --silver-hi: #fafafa;
    --silver-mid: #bdbdbd;
    --silver-lo: #7a7a7a;
  }
  * { box-sizing: border-box; margin: 0; padding: 0; }
  html, body {
    width: 1200px; height: 900px; overflow: hidden;
    background: var(--page-bg);
    font-family: "Lato", Arial, sans-serif;
  }
  .flyer {
    position: absolute; left: 303px; top: 32px;
    width: 593px; height: 835px;
    background: radial-gradient(ellipse at 50% 40%, #262629 0%, var(--flyer-bg) 70%);
    box-shadow: 0 6px 18px rgba(0,0,0,.35);
    overflow: hidden;
  }
  .title {
    position: absolute; left: 22px; top: 22px; width: 300px;
    color: var(--orange); font-weight: 900; font-size: 44px; line-height: 50px;
    text-align: center;
  }
  .month-pill {
    position: absolute; left: 48px; top: 141px; width: 220px; height: 38px;
    border-radius: 6px;
    background: linear-gradient(180deg, var(--silver-hi) 0%, var(--silver-mid) 45%, var(--silver-lo) 55%, #a9a9a9 100%);
    box-shadow: 0 3px 5px rgba(0,0,0,.6);
    color: var(--white); font-weight: 900; font-size: 27px; line-height: 38px; text-align: center;
    text-shadow: 0 1px 2px rgba(0,0,0,.7);
  }
  .brand {
    position: absolute; left: 360px; top: 40px; width: 200px;
    display: flex; flex-direction: column; align-items: center; gap: 12px;
  }
  .brand-dot {
    width: 62px; height: 62px; border-radius: 50%; background: var(--silver-mid);
  }
  .brand-name {
    color: var(--silver-mid); font-weight: 900; font-size: 22px; line-height: 26px; text-align: center;
  }
  .package {
    position: absolute; left: 23px; width: 552px;
    border: 2px solid var(--orange); border-radius: 9px;
    padding: 3px 12px 0 14px;
  }
  .package--one { top: 194px; height: 268px; }
  .package--two { top: 479px; height: 300px; }
  .package-label { color: var(--orange); font-weight: 900; font-size: 24px; line-height: 30px; }
  .price-bar {
    margin: 2px 0 0 -4px; width: 526px; height: 38px; border-radius: 6px;
    background: linear-gradient(180deg, var(--silver-hi) 0%, #d8d8d8 40%, var(--silver-lo) 60%, #c4c4c4 100%);
    box-shadow: 0 3px 5px rgba(0,0,0,.7);
    color: var(--ink); font-weight: 900; font-size: 25px; line-height: 38px; text-align: center;
    letter-spacing: -.2px;
  }
  .package-name { margin-top: 2px; color: var(--orange); font-weight: 900; font-size: 25px; line-height: 28px; }
  .features { list-style: none; margin-top: -2px; }
  .features li {
    position: relative; padding-left: 24px;
    color: var(--white); font-size: 13.5px; line-height: 24.5px;
  }
  .features .burst { position: absolute; left: 4px; top: 4px; width: 16px; height: 16px; }
  .donation-band {
    position: absolute; left: 0; bottom: 0; width: 100%; height: 47px;
    background: var(--orange);
    color: var(--white); font-weight: 700; font-size: 17.5px; line-height: 47px; text-align: center;
  }
</style>
</head>
<body>
<svg width="0" height="0" style="position:absolute">
  <defs>
    <symbol id="burst" viewBox="0 0 20 20">
      <polygon fill="#f58220" points="10,0 11.8,5.6 17,3 14.4,8.2 20,10 14.4,11.8 17,17 11.8,14.4 10,20 8.2,14.4 3,17 5.6,11.8 0,10 5.6,8.2 3,3 8.2,5.6"/>
    </symbol>
  </defs>
</svg>

<main class="flyer">
  <h1 class="title">The Lindqvist Special</h1>
  <div class="month-pill">For August</div>

  <div class="brand">
    <span class="brand-dot"></span>
    <span class="brand-name">Wren Motorcar Polishing</span>
  </div>

  <section class="package package--one">
    <h2 class="package-label">Package 1</h2>
    <div class="price-bar">[Cars $24.99][Trucks Vans &amp; SUV's $34.99]</div>
    <h3 class="package-name">Speed Detail:</h3>
    <ul class="features">
      <li><svg class="burst"><use href="#burst"/></svg>Exterior Pressure Clean w/ Spotless water treatment &nbsp;and Vacuum dried</li>
      <li><svg class="burst"><use href="#burst"/></svg>Wheel Wells Glossed and Cleaned</li>
      <li><svg class="burst"><use href="#burst"/></svg>Tires Cleaned and Hand Dried</li>
      <li><svg class="burst"><use href="#burst"/></svg>Tires Dressed with Gloss Finish</li>
      <li><svg class="burst"><use href="#burst"/></svg>Exterior and Interior Windows cleaned and Hand Dried</li>
      <li><svg class="burst"><use href="#burst"/></svg>Interior is Vacuumed and Door jams cleaned to Perfection!</li>
    </ul>
  </section>

  <section class="package package--two">
    <h2 class="package-label">Package 2</h2>
    <div class="price-bar">[Cars $39.99][Trucks Vans &amp; SUV's $44.99]</div>
    <h3 class="package-name">Speed Detail &amp; Hand Waxing</h3>
    <ul class="features">
      <li><svg class="burst"><use href="#burst"/></svg>Exterior Pressure Clean w/ Spotless water treatment and Vacuum dried</li>
      <li><svg class="burst"><use href="#burst"/></svg>Wheel Wells Glossed and Cleaned</li>
      <li><svg class="burst"><use href="#burst"/></svg>Tires Cleaned and Hand Dried</li>
      <li><svg class="burst"><use href="#burst"/></svg>Tires Dressed with Gloss Finish</li>
      <li><svg class="burst"><use href="#burst"/></svg>Exterior and Interior Windows cleaned and Hand Dried</li>
      <li><svg class="burst"><use href="#burst"/></svg>Interior is Vacuumed and Door jams cleaned to Perfection!</li>
      <li><svg class="burst"><use href="#burst"/></svg>Hand Applied Wax Treatment with Delmark's Advanced Spray on wax &amp;<br>Micro Scratch Sealant!</li>
    </ul>
  </section>

  <footer class="donation-band">A percentage of proceeds will be Donated to Help Veterans in need!</footer>
</main>
</body>
</html>
```